Famous Australian Web Brand (SiteKeyHub.com.au) Needs a New Website & Logo

SiteKeyHub.com.au is one of the leading domain name registration businesses in Australia and is looking for an overhaul of its website and brand.

SiteKeyHub.com.au current products/services include domain name registration, web hosting, web site creation and SSL certificates.

In this design contest on PixelSwarm, we would like designers to create a new logo and new website design for SiteKeyHub.com.au.

Here is what contest entrants will need to create:
- 1 new logo
- 1 new home page design
- 1 internal page (pricing page)

The winning designer will receive the main prize of $750. In addition to this, the winning designer will have the opportunity to work with SiteKeyHub for the build of the full website and may get ongoing design work from SiteKeyHub.
Updates

thank you all for your designs, we are after a web 2.0 look and feel, please dont use serif fonts, lets use modern and sleek ones, i will upload some samples of one we like shortly

header is to be in black with some texturing, white fonts and the call to action buttons are in green.

for the 6 free services, please use round edges for the images with the text under it, as i will upload shortly and we would like custome images, not stockimage types please

im uploading a sample of a background image for the header, which is black with texturing and also and image for the footer/middle of the page which has the correct shading of the grey for the middle section

please see file 8 for the look we are trying to get with our site and for font ideas

Reason: we have decided to extend the contest for another 3 days as a couple of designers have requested a bit more time

Target Market(s)

People that might need to buy a domain name or start a website: small business owners; entrepreneurs; bloggers; everyone from mum-and-dad website owners to tech savvy entrepreneurs. Geographically we will be targeting Australia but this should not influence the design.

Industry/Entity Type

Build

Requirements
Must have
• The logo should:
- Have the text "SiteKeyHub"
- Be positioned in the top left hand corner of the website
- Be either a wordmark, pictorial or abstract logo. That is, text-only logos are acceptable but we are also interested in receiving logos with a mark to the left that could somehow represents the business that we’re in

The homepage should:
- Feel modern, slick, web2.0
- Have a horizontal menu with 4 menu items: About Us | Contact Us | My Cart | Login
- Include the logo at the top
- Include the content from this Word Document
- Include the rough layout and style from this JPG template layout

The interior page should:
- Have the same look and feel as the home page
- Include the rough layout and style from this JPG attachment
- Include the content from this second Word Document
Nice to have
• - Grey, white and black primary colors
- Buttons that are green or lime green with a web2.0 call to action
- Full-width design (i.e. across the screen like PixelSwarm)
Should not have
• - Do not include overt Australian references. While we are an Australian business we do not want Australian flags, kangaroos or Captain Bellwether in our logo or on our website.
- Do not use the current red color scheme in the design. We want to move away from this.

```html
<!DOCTYPE html>
<html lang="en">
<head>
<meta charset="utf-8">
<title>SiteKeyHub – Domain Names</title>
<link rel="stylesheet" href="https://fonts.googleapis.com/css2?family=Source+Sans+3:wght@300;400;600;700;900&display=swap">
<style>
:root{
  --black:#0b0b0b;
  --header-mid:#2a2a2a;
  --white:#ffffff;
  --green:#7fa52a;
  --green-light:#a9cf55;
  --green-dark:#4f7314;
  --heading-green:#8bb23a;
  --text:#6a6a6a;
  --card-top:#f4f4f4;
  --card-bottom:#d9d9d9;
  --card-edge:#c9c9c9;
  --footer-text:#8a8a8a;
  --footer-line:#3a3a3a;
  --page-bg:#f7f7f7;
}
*{box-sizing:border-box;margin:0;padding:0}
html,body{width:857px;height:1200px;overflow:hidden}
body{font-family:"Source Sans 3",Arial,sans-serif;background:var(--page-bg);position:relative;color:var(--text)}
.abs{position:absolute}

/* header */
.site-header{position:absolute;left:0;top:0;width:857px;height:256px;
  background:radial-gradient(ellipse 420px 160px at 428px 120px,#3a3a3a 0%,#161616 60%,var(--black) 100%);}
.site-header::before{content:"";position:absolute;inset:0;
  background-image:repeating-linear-gradient(45deg,rgba(255,255,255,.025) 0 2px,transparent 2px 4px);}
.help-pill{left:93px;top:4px;width:127px;height:16px;border-radius:8px;background:#444;
  color:var(--white);font-size:8.5px;line-height:16px;text-align:center}
.utility-nav{right:116px;top:4px;color:var(--white);font-size:10px;word-spacing:1px}
.brand{left:90px;top:42px;display:flex;align-items:center;gap:9px;color:var(--white);font-size:26px;font-weight:700;letter-spacing:-.3px}
.brand-square{width:24px;height:24px;border:2px solid var(--white);border-radius:2px}
.main-nav{left:380px;top:43px;width:383px;height:35px;border-radius:17px;
  background:linear-gradient(#b6d86a,var(--green) 55%,#5e8a1a);border:1px solid #cfe89a;
  display:flex;justify-content:space-around;align-items:center;padding:0 14px;
  color:var(--white);font-size:12.5px}
.headline{left:0;width:857px;top:103px;text-align:center;color:var(--white);font-size:37px;font-weight:300;letter-spacing:-.6px}
.search-bar{left:97px;top:178px;width:502px;height:43px;border:4px solid var(--green);background:var(--white);
  display:flex;align-items:center;box-shadow:0 0 0 1px #9cc650}
.search-prefix{margin-left:14px;font-size:19px;color:#333}
.search-placeholder{margin-left:6px;font-size:19px;color:#aaa;flex:1}
.tld-select{width:96px;height:100%;border-left:1px solid #bbb;display:flex;align-items:center;justify-content:space-between;padding-left:10px;font-size:19px;color:#333}
.tld-arrow{width:28px;height:33px;background:#111;margin-right:2px;display:flex;align-items:center;justify-content:center}
.search-button{left:622px;top:183px;width:141px;height:36px;border-radius:18px;
  background:linear-gradient(#c3e07a,var(--green) 55%,#5c8719);border:1px solid #d6eda3;
  color:var(--white);font-size:31px;font-weight:900;text-align:center;line-height:32px;letter-spacing:-.5px;
  text-shadow:0 1px 2px rgba(0,0,0,.5)}
.quick-links{top:228px;color:var(--white);font-size:9.5px}

/* body */
.divider{left:0;top:262px;width:857px;height:6px;background:var(--white);border-bottom:1px solid #ccc}
.content{left:0;top:268px;width:857px;height:755px;background:linear-gradient(var(--white),var(--page-bg) 40%,#ececec)}
.intro{left:0;top:304px;width:857px;text-align:center;color:var(--heading-green);font-size:27px;font-weight:900;line-height:36px;
  letter-spacing:-.5px;text-shadow:0 1px 0 #5f8a1c,0 2px 3px rgba(0,0,0,.25)}
.feature{position:absolute;width:213px}
.feature-image{height:123px;border-radius:8px;border:1px solid var(--card-edge);
  background:linear-gradient(var(--card-top),#ececec 60%,var(--card-bottom));box-shadow:0 3px 5px rgba(0,0,0,.15);
  position:relative;overflow:hidden}
.ribbon{position:absolute;left:-22px;top:14px;width:80px;height:16px;background:var(--green);transform:rotate(-45deg);
  color:var(--white);font-size:6.5px;font-weight:700;text-align:center;line-height:16px}
.feature-title{margin:14px 0 0 10px;color:var(--green);font-size:13px;font-weight:600}
.feature-text{margin:6px 0 0 10px;width:200px;font-size:11.3px;line-height:16.5px}

/* footer */
.site-footer{left:0;top:1023px;width:857px;height:177px;background:var(--black)}
.site-footer::before{content:"";position:absolute;inset:0;
  background-image:repeating-linear-gradient(45deg,rgba(255,255,255,.03) 0 2px,transparent 2px 4px)}
.footer-col{position:absolute;top:48px;width:100px}
.footer-col h3{color:var(--green);font-size:12.5px;font-weight:400;margin-bottom:6px}
.footer-col a{display:block;color:var(--footer-text);font-size:8.5px;line-height:14px;border-bottom:1px solid var(--footer-line);text-decoration:none}
.cta-box{position:absolute;left:550px;top:35px;width:214px;height:77px;border-radius:6px;
  background:linear-gradient(#a9cf55,var(--green) 55%,#5b8618);border:1px solid #cfe89a;color:var(--white);text-align:center}
.cta-box p{font-size:15px;margin-top:9px;letter-spacing:-.3px}
.cta-box strong{display:block;font-size:25px;font-weight:900;letter-spacing:-.5px;margin-top:1px}
.copyright{position:absolute;left:552px;top:125px;color:#777;font-size:7.5px}
</style>
</head>
<body>
<header class="site-header">
  <div class="abs help-pill">Have a question? Call 1300 41 72 95</div>
  <nav class="abs utility-nav">Price List | My Cart | About Us | Contact Us | Login</nav>
  <div class="abs brand"><span class="brand-square"></span>SiteKeyHub</div>
  <nav class="abs main-nav"><span>Domains ▾</span><span>Creator</span><span>Email</span><span>Hosting</span><span>Marketing</span></nav>
  <h1 class="abs headline">You get a lot more than just a domain name.</h1>
  <div class="abs search-bar">
    <span class="search-prefix">www.</span>
    <span class="search-placeholder">start your domain search here</span>
    <span class="tld-select">.com<span class="tld-arrow"><svg width="10" height="7" viewBox="0 0 10 7"><path d="M0 0h10L5 7z" fill="#fff"/></svg></span></span>
  </div>
  <div class="abs search-button">search</div>
  <span class="abs quick-links" style="left:152px">Renew a domain</span>
  <span class="abs quick-links" style="left:270px">Transfer a domain</span>
  <span class="abs quick-links" style="left:398px">View Price List</span>
</header>

<div class="abs divider"></div>
<main class="abs content"></main>
<h2 class="abs intro">Everything your business needs to be successful<br>online is FREE with every domain name.</h2>

<section class="feature" style="left:93px;top:421px">
  <div class="feature-image" role="img" aria-label="Site map illustration of linked page icons"><span class="ribbon">JUST RELEASED</span></div>
  <h3 class="feature-title">15 Page Website</h3>
  <p class="feature-text">Create a professional, full-featured website in minutes without any technical knowledge. Choose from 4,000+ stunning website designs and customize your site with near-limitless options. Upload your own artwork for a truly personalised look.</p>
</section>
<section class="feature" style="left:321px;top:421px">
  <div class="feature-image" role="img" aria-label="Illustration of a contact figure beside an envelope"><span class="ribbon">JUST RELEASED</span></div>
  <h3 class="feature-title">Professional Email</h3>
  <p class="feature-text">Having a personalised address that matches your domain name (for example, Sam@SamsMuffins.com or Sales@SamsMuffins.com) gives your company a much more professional image when you communicate with customers and associates.</p>
</section>
<section class="feature" style="left:550px;top:421px">
  <div class="feature-image" role="img" aria-label="Illustration of a server unit with tools"></div>
  <h3 class="feature-title">Website Hosting</h3>
  <p class="feature-text">We provide the fast and secure hosting for your website. We take care of all the maintenance so all you have to do is create content for your site. Best of all, you don't have to pay a cent for hosting for as long as your domain is registered with us.</p>
</section>
<section class="feature" style="left:93px;top:735px">
  <div class="feature-image" role="img" aria-label="Illustration of a magnifying glass with rising arrows"></div>
  <h3 class="feature-title">Search Engine Optimization</h3>
  <p class="feature-text">What good is the best looking website if no one visits it? We thought about that too! All our sites are optimised for search engines by default to ensure that your website is found by Searchly and other search engines like Findora and Lookwise.</p>
</section>
<section class="feature" style="left:321px;top:735px">
  <div class="feature-image" role="img" aria-label="Illustration of a phone handset between two people"></div>
  <h3 class="feature-title">Business Class Support</h3>
  <p class="feature-text">This is a point of pride for us and we are here to help. We're available to you 24 hours a day, everyday. Many of our competitors don't even provide a phone number for you to call! You deserve the best, and we won't settle for providing anything less.</p>
</section>
<section class="feature" style="left:550px;top:735px">
  <div class="feature-image" role="img" aria-label="Illustration of a calendar with a dollar sign"></div>
  <h3 class="feature-title">Renewal Price</h3>
  <p class="feature-text">You'll never pay more to renew your domain name than the rate you paid when you initially registered it, or what our registration rate was when you transferred. (The only exceptions would be if you took advantage of a limited-time, special price)</p>
</section>

<footer class="abs site-footer">
  <div class="footer-col" style="left:93px"><h3>DOMAIN NAMES</h3><a>Overview</a><a>Pricing</a><a>Renew</a><a>Transfer</a></div>
  <div class="footer-col" style="left:208px"><h3>DOMAIN NAMES</h3><a>Overview</a><a>Pricing</a><a>Renew</a><a>Transfer</a></div>
  <div class="footer-col" style="left:323px"><h3>DOMAIN NAMES</h3><a>Overview</a><a>Pricing</a><a>Renew</a><a>Transfer</a></div>
  <div class="cta-box"><p>HAVE A QUESTION FOR US?</p><strong>Call 1300 41 72 95</strong></div>
  <p class="copyright">Copyright 2003-2010, WebMint, Pty Ltd.</p>
</footer>
</body>
</html>
```